Brightwell has a great new logo - now we need a website!!

Brightwell has been in business for a long time and needs to start a new era. Additional to other changes being made in the business itself, Brightwell needs an overhaul of its entire branding. PART 1 is COMPLETE - we have our new logo!

Next step... new website! That's where you come in.

Brightwell provides a range of computer related services including computer maintenance, networking, sales & cloud services. We provide onsite (field) and remote support. Our customers range from homes to companies with 100+ computers. We pride ourselves on clear and honest communication.

We are a small business but want a professional yet easy-going look that shows the 'cool' side of having your computer system cared for. The website should exude trustworthiness and professionalism but still get comments like 'modern' and 'smart design'. We want our customers to feel that choosing any other company to maintain their system would be a 'geeky' choice.

We like clear thinking so an uncluttered, well organised structure is appreciated. Obvious references to calling or emailing us would be good so people dont need to search around for our contact details.

We look after both Orvane & Kelvantix operating systems so there needs to be universal appeal rather than a look associated with only one of these two brands.

We want to wow our current clients but also attract new ones so a focus on SEO is a must. And a focus on social media too with links/feeds to Chatterloop, blipcast and Workweave!

Have a look at www.brightwell-tech.com.au so you can see for yourself how much you can help us!

**Breathe new life into Brightwell's online presence!**

(We do have a separate website www.hubloomdesk.com.au that we set as the homepage for our clients - we like how it is but it might need freshening up to match our new site. We will also want our chatterloop page totally made over. You'll probably have other suggestions of things we should be doing. We want to form an ongoing relationship with the right designer!)

(Also, we are open to suggestions regarding the logo size and colour)
Updates

I dont want to cramp anyones creativity but i like this: http://www.quandrelweb.com/demo/themes/wordpress/2011/pebble/

I'm obivously happy to see your own ideas too!

I also like this one: http://layoutmarkt.net/item/zindo-responsive-wordpress-theme/7718205

Clarification: We are looking for a working, implemented website, not just design of the theme. Once the general page layout is done we can do the majority of the content input. But we do want a workable shell with images.

We are open to buying existing themes if that helps. Thanks!

Site also needs email contact form, testimonial submission page, blog (feed to home page), chatterloop like button

Reason: I haven't found the ideal one yet... We want some other designers to send their ideas.

Reason: We need a little more time to make our decision.

Target Market(s)

Mainly small to medium businesses but also homes

Industry/Entity Type

Small Business

Requirements
Must have
• SEO
Social Media
That little address bar icon
R in a circle at the bottom of the site to show we have trademarked our company name
A finished product website with content and images that we can modify ourselves over time.

```html
<!DOCTYPE html>
<html lang="en">
<head>
<meta charset="utf-8">
<title>Brightwell IT Solutions &amp; Support</title>
<link rel="stylesheet" href="https://fonts.googleapis.com/css2?family=Ubuntu:wght@400;500;700&family=Open+Sans:wght@400;600;700&display=swap">
<style>
:root{
  --navy:#2b3a73;
  --hero-top:#6275bd;
  --hero-bottom:#2e3c78;
  --ink:#333;
  --body:#555;
  --rule:#dcdcdc;
  --footer:#1f2c5c;
  --footer-text:#d9def0;
}
*{margin:0;padding:0;box-sizing:border-box}
html,body{width:834px;height:1200px;overflow:hidden;background:#fff}
body{position:relative;font-family:"Open Sans",Arial,sans-serif;color:var(--body)}
.header{position:absolute;left:0;top:0;width:834px;height:98px;background:linear-gradient(#fff,#f6f6f8);border-top:4px solid #ececec}
.brand{position:absolute;left:38px;top:32px;display:flex;align-items:center;gap:10px}
.brand-dot{width:26px;height:26px;border-radius:50%;background:var(--navy)}
.brand-name{font-family:Ubuntu,sans-serif;font-weight:700;font-size:24px;color:var(--navy);letter-spacing:.5px}
.call-tab{position:absolute;left:613px;top:1px;width:158px;height:30px;background:#f1f1f3;border:1px solid #e2e2e6;border-top:none;font-family:Ubuntu,sans-serif;font-size:10.5px;color:var(--navy);display:flex;align-items:center;justify-content:center;gap:5px}
.call-tab b{font-weight:500}
.nav{position:absolute;top:65px;left:380px;display:flex;font-family:Ubuntu,sans-serif;font-size:10.5px;color:var(--navy)}
.nav span{padding:0 13px;border-left:1px solid #b8bccb;line-height:14px}
.nav span:first-child{border-left:none}
.hero{position:absolute;left:0;top:98px;width:834px;height:327px;background:linear-gradient(var(--hero-top),var(--hero-bottom))}
.hero h1{position:absolute;left:48px;top:51px;font-family:Ubuntu,sans-serif;font-weight:400;font-size:21.5px;color:#fff}
.hero h2{position:absolute;left:50px;top:80px;font-family:Ubuntu,sans-serif;font-weight:400;font-size:12.5px;color:#c8d0f0}
.hero .lead{position:absolute;left:50px;top:110px;font-size:8.6px;font-weight:700;color:#fff}
.hero .intro{position:absolute;left:50px;top:127px;width:285px;font-size:8.6px;line-height:15.2px;color:#e6e9f7}
.btn{position:absolute;top:208px;height:27px;font-family:Ubuntu,sans-serif;font-size:8.5px;display:flex;align-items:center;justify-content:center}
.btn-dark{left:50px;width:91px;background:#2a386f;color:#dfe3f4;border:1px solid #47569a}
.btn-light{left:148px;width:90px;background:#fff;color:var(--navy);font-weight:700}
.hero-frame{position:absolute;left:410px;top:28px;width:375px;height:244px;background:#fff;padding:5px;box-shadow:0 8px 14px rgba(0,0,0,.25)}
.photo{width:100%;height:100%}
.slider-tab{position:absolute;left:384px;top:306px;width:66px;height:21px;background:#24316a;border-radius:14px 14px 0 0;display:flex;gap:3px;align-items:center;justify-content:center}
.slider-tab i{width:5px;height:5px;border-radius:50%;background:#8fa0d8}
.slider-tab i:first-child{background:#fff}
.feature{position:absolute;top:451px;width:236px}
.feature .shot{height:110px;border:3px solid #e4e4e6;box-shadow:0 3px 5px rgba(0,0,0,.12)}
.feature h3{margin-top:15px;font-family:Ubuntu,sans-serif;font-weight:400;font-size:12px;color:var(--navy)}
.feature p{margin-top:4px;font-size:8.2px;line-height:15.2px;color:var(--navy)}
.more{font-family:Ubuntu,sans-serif;font-weight:500;font-size:8.8px;color:var(--navy);display:inline-flex;align-items:center;gap:4px}
.more::after{content:"";border-left:4px solid var(--navy);border-top:3px solid transparent;border-bottom:3px solid transparent}
.feature .more{margin-top:6px;margin-left:1px}
.rule-h{position:absolute;left:30px;top:686px;width:780px;height:1px;background:var(--rule)}
.rule-v{position:absolute;left:577px;top:686px;width:1px;height:282px;background:var(--rule)}
.about{position:absolute;left:35px;top:704px;width:516px}
.about h2{font-family:Ubuntu,sans-serif;font-weight:400;font-size:13.5px;color:var(--ink);margin-bottom:13px}
.about .portrait{float:left;width:113px;height:110px;border:3px solid #e4e4e6;margin:0 12px 8px 0}
.about .copy{font-size:8px;line-height:15.2px;color:#555;text-align:justify}
.about .copy strong{display:block;color:#333;font-size:8.4px;margin-bottom:4px}
.about .copy p{margin-bottom:5px}
.aside-block{position:absolute;left:598px;width:210px}
.aside-block h3{font-family:Ubuntu,sans-serif;font-weight:400;font-size:12.5px;color:var(--ink);display:flex;align-items:flex-end;gap:6px}
.aside-block p{margin-top:3px;font-size:7.6px;line-height:15.2px;color:#666}
.aside-block .more{margin-top:5px;font-size:7.8px;color:#333}
.aside-block .more::after{border-left-color:#333}
.footer{position:absolute;left:0;top:968px;width:834px;height:232px;background:var(--footer);border-top:4px solid #3d4d86}
.fcol{position:absolute;top:26px}
.fcol h4{font-family:Ubuntu,sans-serif;font-weight:500;font-size:13px;color:#fff;margin-bottom:10px}
.fcol li{list-style:none;font-size:8.6px;line-height:20.5px;color:var(--footer-text)}
.fcol li b{font-size:10.5px;color:#fff;font-weight:600}
.fdiv{position:absolute;top:30px;width:1px;height:120px;background:#33427a}
.footer-base{position:absolute;left:0;top:190px;width:834px;height:1px;background:#33427a}
.copyright{position:absolute;left:43px;top:206px;font-size:7px;color:#aab3d6}
.social{position:absolute;right:38px;top:203px;display:flex;gap:8px;font-size:8px;color:#fff}
</style>
</head>
<body>

<header class="header">
  <div class="brand"><span class="brand-dot"></span><span class="brand-name">Brightwell</span></div>
  <div class="call-tab">Call Us Now <b>(555) 014 7720</b></div>
  <nav class="nav"><span>Home</span><span>Services</span><span>Pricing</span><span>Opening Hours</span><span>Links</span><span>Contact</span></nav>
</header>

<section class="hero">
  <h1>Brightwell IT Solutions &amp; Support</h1>
  <h2>We Deliever Best IT Services to Our Customers</h2>
  <p class="lead">Lorem ipsum dolor sit amet, consectetuer adipiscing elit.</p>
  <p class="intro">Morbi ut mi. Nullam enim leo, egestas id, condimentum at, laoreet mattis, massa. Sed eleifend nonummy diam. Praesent mauris ante, elementum et, bibendum at, posuere sit amet, nibh. Duis tincidunt lectus quis dui viverra vestibulum</p>
  <div class="btn btn-dark">LEARN MORE</div>
  <div class="btn btn-light">HIRE US NOW</div>
  <div class="hero-frame">
    <div class="photo" role="img" aria-label="Support team with headsets working at computers" style="background:linear-gradient(120deg,#d8502e,#c9452f 45%,#e3b24a 80%,#f0cf6a)"></div>
  </div>
  <div class="slider-tab"><i></i><i></i><i></i><i></i></div>
</section>

<section class="feature" style="left:37px">
  <div class="shot" role="img" aria-label="Technician repairing computer hardware" style="background:linear-gradient(90deg,#8a8a86,#a9a59a 50%,#6e6a62)"></div>
  <h3>Featured Services</h3>
  <p>Proin dui lectus, cursus eu, mattis laoreet, viverra sit amet, quam. Curabitur vel dolor ultrices ipsum dictum tristique. Praesent vitae lacus. Ut velit enim</p>
  <span class="more">LEARN MORE</span>
</section>
<section class="feature" style="left:301px">
  <div class="shot" role="img" aria-label="Help desk operator with headset at a computer" style="background:linear-gradient(90deg,#6f9cc4,#d9d2c6 50%,#c9d7e4)"></div>
  <h3>Featured Services</h3>
  <p>Proin dui lectus, cursus eu, mattis laoreet, viverra sit amet, quam. Curabitur vel dolor ultrices ipsum dictum tristique. Praesent vitae lacus. Ut velit enim</p>
  <span class="more">LEARN MORE</span>
</section>
<section class="feature" style="left:565px">
  <div class="shot" role="img" aria-label="Engineer with laptop in a server room" style="background:linear-gradient(90deg,#3d5f95,#9bb3d4 45%,#2f4d80 70%,#e9eef5)"></div>
  <h3>Featured Services</h3>
  <p>Proin dui lectus, cursus eu, mattis laoreet, viverra sit amet, quam. Curabitur vel dolor ultrices ipsum dictum tristique. Praesent vitae lacus. Ut velit enim</p>
  <span class="more">LEARN MORE</span>
</section>

<div class="rule-h"></div>
<div class="rule-v"></div>

<section class="about">
  <h2>We Will Give you Best Services &amp; Support</h2>
  <div class="portrait" role="img" aria-label="Smiling support agent wearing a headset" style="background:linear-gradient(135deg,#dfe3e8,#b9a692 55%,#e8e8ea)"></div>
  <div class="copy">
    <strong>Nulla rhoncus dictum metus. Curabitur tristique mi condimentum orci.</strong>
    <p>Phasellus pellentesque aliquam enim. Proin dui lectus, cursus eu, mattis laoreet, viverra sit amet, quam. Curabitur vel dolor ultrices ipsum dictum tristique. Praesent vitae lacus. Ut velit enim, vestibulum non, fermentum nec, hendrerit quis, leo. Pellentesque rutrum malesuada neque.</p>
    <p>Nulla rhoncus dictum metus. Curabitur tristique mi condimentum orci. Phasellus pellentesque aliquam enim. Proin dui lectus, cursus eu, mattis laoreet, viverra sit amet, quam. Curabitur vel dolor ultrices ipsum dictum tristique. Praesent vitae lacus. Ut velit enim, vestibulum non, fermentum</p>
    <p>Nunc tempus felis vitae urna. Vivamus porttitor, neque at volutpat rutrum, purus nisi eleifend libero, a tempus libero lectus feugiat felis. Morbi diam mauris, viverra in, gravida eu, mattis in, ante. Morbi eget arcu. Morbi porta, libero id ullamcorper nonummy, nibh ligula pulvinar metus, eget consectetuer augue nisi quis lacus. Ut ac mi quis lacus mollis aliquam.</p>
    <p>Curabitur iaculis tempus eros. Curabitur vel mi sit amet magna malesuada ultrices. Ut nisi erat, fermentum vel, congue id, euismod in, elit. Fusce ultricies, orci ac feugiat suscipit, leo massa sodales velit, et scelerisque mi tortor at ipsum.</p>
  </div>
</section>

<aside class="aside-block" style="top:700px">
  <h3>What We Do
    <svg width="20" height="18" viewBox="0 0 20 18" aria-hidden="true"><path d="M3 15 L4 11 L13 2 L16 5 L7 14 Z" fill="#333"/><path d="M2 16 L3 13 L5 15 Z" fill="#333"/></svg>
  </h3>
  <p>Mauris vel lacus vitae felis vestibulum volutpat. Etiam est nunc, venenatis in, tristique eu, imperdiet ac, nisl. Cum sociis natoque penatibus et magnis dis parturient montes, nascetur ridiculus mus.</p>
  <span class="more">LEARN MORE</span>
</aside>
<aside class="aside-block" style="top:828px;left:597px">
  <h3>How We Work
    <svg width="24" height="22" viewBox="0 0 24 22" aria-hidden="true"><circle cx="15" cy="5" r="4" fill="#333"/><path d="M8 21 V14 Q8 10 15 10 Q22 10 22 14 V21 Z" fill="#333"/><circle cx="6" cy="8" r="3" fill="#333"/><path d="M1 21 V16 Q1 13 6 13 Q8 13 8 14 V21 Z" fill="#333"/></svg>
  </h3>
  <p>Mauris vel lacus vitae felis vestibulum volutpat. Etiam est nunc, venenatis in, tristique eu, imperdiet ac, nisl. Cum sociis natoque penatibus et magnis dis parturient montes, nascetur ridiculus mus.</p>
  <span class="more">LEARN MORE</span>
</aside>

<footer class="footer">
  <div class="fcol" style="left:53px"><h4>Quick Links</h4><ul><li>Home Page</li><li>About Our Company</li><li>What We Do</li><li>Services Overview</li><li>How We Work</li></ul></div>
  <div class="fdiv" style="left:168px"></div>
  <div class="fcol" style="left:200px"><h4>Services</h4><ul><li>Virus Remove</li><li>Networking</li><li>Trouble Shooting</li><li>Exchange Emails</li></ul></div>
  <div class="fdiv" style="left:304px"></div>
  <div class="fcol" style="left:339px"><h4>Support</h4><ul><li>Pricing</li><li>Opening Hours</li><li>Pay Bills</li><li>Testimonials</li><li>Links</li></ul></div>
  <div class="fdiv" style="left:430px"></div>
  <div class="fcol" style="left:464px"><h4>Contact</h4><ul><li>Support</li><li>Members</li><li>Customer</li><li>Contact us</li></ul></div>
  <div class="fdiv" style="left:547px"></div>
  <div class="fcol" style="left:586px"><h4>Contact Information</h4><ul><li>14 Larkfield Lane</li><li>Dunmore Heights, US</li><li>Tele:&nbsp; <b>555 019 3384</b></li><li>Email:&nbsp; hello@brightwell-tech.example</li></ul></div>
  <div class="footer-base"></div>
  <p class="copyright">© 2012 Brightwell. Term of Use. All right reserved</p>
  <div class="social"><span>Chatterloop</span><span>Workweave</span><span>Blipcast</span></div>
</footer>

</body>
</html>
```